Employee Benefits Flyer for Recruiting

We are a Steel Product Supplier and Manufacturer in Toledo Ohio.

We would like to create an "attention getting", one-page handout to give prospective employees (both production and administrative) that illustrates all the benefits we offer as a company. An editable document would be preferable as we add more or change existing benefits in the future. Current benefits include:

Individual and Family Medical Insurance
Dental Insurance
Vision Insurance
Short Term Disability Insurance
Critical Illness and Accident Insurance
No Cost Life Insurance Policy
Education Cost Reimbursement
401K with Company Match
Profit Sharing
Attendance and Performance Bonuses
No Cost Legal Assistance
No Cost Counseling Services
No Cost Tobacco Cessation Coaching
No Cost College Planning Assistance
No Cost Work-Life Services
No Cost Employee Discounts
No Cost Legal Consultation
No Cost Financial Consultation
No Cost ID Theft Assistance
No Cost Tax Consultation Assistance
Up to 17 Days of Paid Time Off

Target Market(s)

Potential Employees

Industry/Entity Type

Industrial Manufacturing

Requirements
Must have
• Nicely laid out illustrations / engaging content

```html
<!DOCTYPE html>
<html lang="en">
<head>
<meta charset="utf-8">
<title>Keystone Steel Works – Employee Benefits Flyer</title>
<link href="https://fonts.googleapis.com/css2?family=Archivo+Black&family=Open+Sans:wght@300;400;600;700&display=swap" rel="stylesheet">
<style>
  :root {
    --page-bg: #dcdcdc;
    --ink-dark: #1f1f20;
    --ink-footer: #141415;
    --brand-blue: #1a5ee6;
    --brand-blue-deep: #0f47c2;
    --metal-light: #eeeff0;
    --metal-mid: #d9dadc;
    --text-dark: #1d1d1f;
    --white: #ffffff;
    --rule: #b9bbbf;
  }
  * { margin: 0; padding: 0; box-sizing: border-box; }
  html, body { width: 800px; height: 1200px; overflow: hidden; }
  body { background: var(--page-bg); font-family: "Open Sans", Arial, sans-serif; position: relative; }

  .flyer {
    position: absolute; left: 20px; top: 108px; width: 760px; height: 984px;
    background: linear-gradient(180deg, var(--metal-light) 0%, var(--metal-mid) 45%, var(--metal-light) 100%);
    box-shadow: 0 6px 18px rgba(0,0,0,.25);
    overflow: hidden;
  }

  .header { position: absolute; left: 0; top: 0; width: 760px; height: 318px; background: var(--ink-dark); }
  .header-photo { position: absolute; left: 0; top: 0; width: 760px; height: 318px; }

  .brand { position: absolute; left: 52px; top: 36px; display: flex; align-items: center; gap: 10px; }
  .brand-dot { width: 26px; height: 26px; border-radius: 50%; background: var(--brand-blue); }
  .brand-name { font-family: "Open Sans", Arial, sans-serif; font-weight: 700; font-size: 17px; letter-spacing: .5px; color: var(--brand-blue); }

  .headline { position: absolute; left: 45px; top: 150px; color: var(--white); }
  .headline-lead { font-family: "Open Sans", Arial, sans-serif; font-weight: 300; font-size: 54px; line-height: 1; letter-spacing: -1px; }
  .headline-main { font-family: "Archivo Black", Arial, sans-serif; font-size: 82px; line-height: .95; color: var(--brand-blue); letter-spacing: -1px; margin-top: 2px; }
  .headline-sub { font-weight: 400; font-size: 20px; letter-spacing: .2px; margin-top: 4px; }

  .benefits-banner { position: absolute; left: 124px; top: 326px; width: 512px; height: 74px; }
  .benefits-title {
    position: absolute; left: 124px; top: 326px; width: 512px; height: 70px;
    display: flex; align-items: center; justify-content: center;
    font-family: "Archivo Black", Arial, sans-serif; font-size: 34px; color: var(--white); letter-spacing: 1px;
  }

  .benefit-list { position: absolute; top: 418px; list-style: none; }
  .benefit-list.left { left: 48px; }
  .benefit-list.right { left: 420px; }
  .benefit { display: flex; align-items: center; height: 41px; font-weight: 600; font-size: 13.5px; color: var(--text-dark); }
  .benefit svg { width: 28px; height: 28px; margin-right: 18px; flex: none; }

  .column-rule { position: absolute; left: 384px; top: 428px; width: 1px; height: 430px; background: var(--rule); }

  .footer-stripe { position: absolute; left: 0; top: 874px; width: 760px; height: 7px; background: var(--brand-blue); }
  .footer { position: absolute; left: 0; top: 881px; width: 760px; height: 103px; background: linear-gradient(180deg, #222325, var(--ink-footer)); }
  .call-label { position: absolute; left: 45px; top: 16px; font-family: "Archivo Black", Arial, sans-serif; font-size: 23px; color: var(--brand-blue); }
  .call-number { position: absolute; left: 45px; top: 42px; font-family: "Archivo Black", Arial, sans-serif; font-size: 38px; color: var(--white); letter-spacing: 1px; }
  .footer-rule { position: absolute; left: 385px; top: 20px; width: 2px; height: 60px; background: var(--white); opacity: .85; }
  .contact { position: absolute; left: 420px; display: flex; align-items: center; gap: 14px; color: var(--white); font-weight: 600; font-size: 20px; }
  .contact.email { top: 14px; }
  .contact.web { top: 48px; }
  .contact svg { width: 20px; height: 20px; }
</style>
</head>
<body>
  <main class="flyer">
    <section class="header">
      <svg class="header-photo" viewBox="0 0 760 318" role="img" aria-label="Aerial photograph of the company's steel building with blue metal roof and siding">
        <defs>
          <linearGradient id="photoTone" x1="0" y1="0" x2="1" y2="1">
            <stop offset="0" stop-color="#9ea3ab"/>
            <stop offset=".45" stop-color="#2f6fb3"/>
            <stop offset=".8" stop-color="#3a72b0"/>
            <stop offset="1" stop-color="#6f7a62"/>
          </linearGradient>
        </defs>
        <polygon points="339,0 760,0 760,318 402,318" fill="url(#photoTone)"/>
        <polygon points="333,0 341,0 404,318 396,318" fill="var(--brand-blue)"/>
      </svg>

      <div class="brand">
        <span class="brand-dot"></span>
        <span class="brand-name">KEYSTONE STEEL WORKS</span>
      </div>

      <div class="headline">
        <div class="headline-lead">WE ARE</div>
        <div class="headline-main">HIRING</div>
        <div class="headline-sub">PRODUCTION &amp; ADMINISTRATIVE</div>
      </div>
    </section>

    <svg class="benefits-banner" viewBox="0 0 512 74" aria-hidden="true">
      <path d="M4 0 H508 L488 60 Q484 70 472 70 H40 Q28 70 24 60 Z" fill="#9aa3b3" opacity=".55" transform="translate(0,4)"/>
      <path d="M0 0 H512 L492 58 Q488 68 476 68 H36 Q24 68 20 58 Z" fill="var(--brand-blue)"/>
    </svg>
    <h2 class="benefits-title">EMPLOYEE BENEFITS</h2>

    <svg width="0" height="0" style="position:absolute" aria-hidden="true">
      <symbol id="icon-check" viewBox="0 0 28 28">
        <path d="M14 2 L24 6 V13 C24 20 19 24 14 26 C9 24 4 20 4 13 V6 Z" fill="none" stroke="var(--brand-blue)" stroke-width="1.6" stroke-linejoin="round"/>
        <path d="M9 14 L13 18 L19 10" fill="none" stroke="var(--brand-blue-deep)" stroke-width="1.8" stroke-linecap="round" stroke-linejoin="round"/>
      </symbol>
    </svg>

    <ul class="benefit-list left">
      <li class="benefit"><svg><use href="#icon-check"/></svg>Individual and Family Medical Insurance</li>
      <li class="benefit"><svg><use href="#icon-check"/></svg>Dental Insurance</li>
      <li class="benefit"><svg><use href="#icon-check"/></svg>Vision Insurance</li>
      <li class="benefit"><svg><use href="#icon-check"/></svg>Short Term Disability Insurance</li>
      <li class="benefit"><svg><use href="#icon-check"/></svg>Critical Illness and Accident Insurance</li>
      <li class="benefit"><svg><use href="#icon-check"/></svg>No Cost Life Insurance Policy</li>
      <li class="benefit"><svg><use href="#icon-check"/></svg>Education Cost Reimbursement</li>
      <li class="benefit"><svg><use href="#icon-check"/></svg>401K with Company Match</li>
      <li class="benefit"><svg><use href="#icon-check"/></svg>Profit Sharing</li>
      <li class="benefit"><svg><use href="#icon-check"/></svg>Attendance and Performance Bonuses</li>
      <li class="benefit"><svg><use href="#icon-check"/></svg>No Cost Legal Assistance</li>
    </ul>

    <div class="column-rule"></div>

    <ul class="benefit-list right">
      <li class="benefit"><svg><use href="#icon-check"/></svg>No Cost Counseling Services</li>
      <li class="benefit"><svg><use href="#icon-check"/></svg>No Cost Tobacco Cessation Coaching</li>
      <li class="benefit"><svg><use href="#icon-check"/></svg>No Cost College Planning Assistance</li>
      <li class="benefit"><svg><use href="#icon-check"/></svg>No Cost Work-Life Services</li>
      <li class="benefit"><svg><use href="#icon-check"/></svg>No Cost Employee Discounts</li>
      <li class="benefit"><svg><use href="#icon-check"/></svg>No Cost Legal Consultation</li>
      <li class="benefit"><svg><use href="#icon-check"/></svg>No Cost Financial Consultation</li>
      <li class="benefit"><svg><use href="#icon-check"/></svg>No Cost ID Theft Assistance</li>
      <li class="benefit"><svg><use href="#icon-check"/></svg>No Cost Tax Consultation Assistance</li>
      <li class="benefit"><svg><use href="#icon-check"/></svg>Up to 17 Days of Paid Time Off</li>
    </ul>

    <div class="footer-stripe"></div>
    <footer class="footer">
      <div class="call-label">CALL US NOW!</div>
      <div class="call-number">800–555–0142</div>
      <div class="footer-rule"></div>
      <div class="contact email">
        <svg viewBox="0 0 20 20" aria-hidden="true"><rect x="2" y="4" width="16" height="12" rx="1" fill="var(--brand-blue)"/><path d="M2 5 L10 11 L18 5" fill="none" stroke="#0b2f80" stroke-width="1.4"/></svg>
        <span>info@keystone-steelworks.com</span>
      </div>
      <div class="contact web">
        <svg viewBox="0 0 20 20" aria-hidden="true"><circle cx="10" cy="10" r="8" fill="none" stroke="var(--brand-blue)" stroke-width="1.6"/><ellipse cx="10" cy="10" rx="3.5" ry="8" fill="none" stroke="var(--brand-blue)" stroke-width="1.4"/><path d="M2 10 H18 M3.5 6 H16.5 M3.5 14 H16.5" stroke="var(--brand-blue)" stroke-width="1.2"/></svg>
        <span>www.keystone-steelworks.com</span>
      </div>
    </footer>
  </main>
</body>
</html>
```